Business Card and Simple Logo Desgin

New Zealand based start up company "Brook Advisory LTD" requires business cards and simple logo design.

Card Content.

Brook Advisory LTD

Joanna Pritchard
CA, BMS (Hons)

j.pritchard@brookadvisory.co.nz
PH +64 21 574 160

Target Market(s)

Corporate Business in IT, Finance and accounting.

Industry/Entity Type

Business

```html
<!DOCTYPE html>
<html lang="en">
<head>
<meta charset="utf-8">
<title>Brook Advisory LTD – Business Card</title>
<link rel="stylesheet" href="https://fonts.googleapis.com/css2?family=Arimo:wght@400;700&display=swap">
<style>
  :root {
    --page-bg: #eceef0;
    --blue-deep: #1583d6;
    --blue-mid: #2f9ee8;
    --blue-light: #5cbcf2;
    --paper: #ffffff;
    --paper-shade: #e6e8ea;
    --brand-blue: #1a74c4;
    --name-yellow: #ffe23a;
    --text-white: #ffffff;
    --card-shadow: rgba(20, 40, 70, 0.22);
  }
  * { box-sizing: border-box; margin: 0; padding: 0; }
  html, body {
    width: 1200px;
    height: 898px;
    overflow: hidden;
    background: var(--page-bg);
    font-family: "Arimo", Arial, sans-serif;
  }
  .canvas {
    width: 1200px;
    height: 898px;
    display: flex;
    flex-direction: column;
    align-items: center;
    justify-content: center;
    gap: 44px;
  }
  .card {
    position: relative;
    width: 600px;
    height: 366px;
    border-radius: 4px;
    overflow: hidden;
    box-shadow: 0 10px 28px var(--card-shadow);
  }
  .card-art {
    position: absolute;
    inset: 0;
    width: 100%;
    height: 100%;
  }

  /* Brand side */
  .card--brand {
    background: linear-gradient(160deg, var(--blue-light) 0%, var(--blue-mid) 45%, var(--blue-deep) 100%);
  }
  .brand-lockup {
    position: absolute;
    left: 0;
    right: 0;
    top: 150px;
    display: flex;
    align-items: center;
    justify-content: center;
    gap: 14px;
    color: var(--text-white);
    font-weight: 700;
    font-size: 30px;
    line-height: 1;
  }
  .brand-square {
    width: 30px;
    height: 30px;
    background: var(--text-white);
    flex: none;
  }

  /* Contact side */
  .card--contact {
    background: linear-gradient(180deg, var(--paper) 0%, var(--paper-shade) 100%);
  }
  .contact-block {
    position: absolute;
    left: 36px;
    top: 40px;
    color: var(--text-white);
  }
  .contact-name {
    color: var(--name-yellow);
    font-weight: 700;
    font-size: 22px;
    margin-bottom: 14px;
  }
  .contact-line {
    font-size: 18px;
    line-height: 1.3;
  }
  .footer-lockup {
    position: absolute;
    right: 36px;
    bottom: 34px;
    display: flex;
    align-items: center;
    gap: 10px;
    color: var(--brand-blue);
    font-weight: 700;
    font-size: 19px;
    line-height: 1;
  }
  .footer-square {
    width: 20px;
    height: 20px;
    background: var(--brand-blue);
    flex: none;
  }
</style>
</head>
<body>
<main class="canvas">

  <section class="card card--brand" aria-label="Business card, brand side">
    <svg class="card-art" viewBox="0 0 600 366" aria-hidden="true">
      <defs>
        <linearGradient id="brand-sheen" x1="0" y1="0" x2="1" y2="0">
          <stop offset="0" stop-color="#ffffff" stop-opacity="0"/>
          <stop offset="0.5" stop-color="#ffffff" stop-opacity="0.12"/>
          <stop offset="1" stop-color="#ffffff" stop-opacity="0"/>
        </linearGradient>
      </defs>
      <rect x="0" y="0" width="600" height="366" fill="url(#brand-sheen)"/>
    </svg>
    <div class="brand-lockup">
      <span class="brand-square"></span>
      <span class="brand-name">Brook Advisory LTD</span>
    </div>
  </section>

  <section class="card card--contact" aria-label="Business card, contact side">
    <svg class="card-art" viewBox="0 0 600 366" aria-hidden="true">
      <defs>
        <linearGradient id="band-fill" x1="0" y1="0" x2="1" y2="1">
          <stop offset="0" stop-color="#5cbcf2"/>
          <stop offset="0.5" stop-color="#2f9ee8"/>
          <stop offset="1" stop-color="#1583d6"/>
        </linearGradient>
      </defs>
      <path d="M0 0 H600 V60 Q460 140 300 180 Q150 215 0 250 Z" fill="url(#band-fill)"/>
    </svg>
    <div class="contact-block">
      <p class="contact-name">Joanna Pritchard CA, BMS (Hons)</p>
      <p class="contact-line">j.pritchard@brookadvisory.co.nz</p>
      <p class="contact-line">PH +64 21 574 160</p>
    </div>
    <div class="footer-lockup">
      <span class="footer-square"></span>
      <span class="footer-name">Brook Advisory LTD</span>
    </div>
  </section>

</main>
</body>
</html>
```